The Quillmore Daily Ledger

I am making a journal for tracking pain symptoms for TMJ (Jaw) pain. I have the cover designed and I just need the journal page designed that will repeat throughout the journal. The journal is the image on the left of the bundle. The page I would like to be developed is the picture that I hand sketched out. It should be a 6 x 9 page, similar to the attached example. Greyscale, no color. Thank you!

Target Market(s)

20-55 year old women

Industry/Entity Type

Healthcare

Colors

Designer to choose only greyscale colors for use in the design.

Requirements
Must have
• A neat, well-designed page with the content I have sketched out by hand.
Nice to have
• Creative display of the content I provided and development of the pain scale and pain diagram faces in a professional looking way.

```html
<!DOCTYPE html>
<html lang="en">
<head>
<meta charset="utf-8">
<title>The Quillmore Daily Ledger – Journal Page</title>
<link rel="stylesheet" href="https://fonts.googleapis.com/css2?family=Open+Sans:wght@400;600;700&family=Montserrat:wght@600&display=swap">
<style>
:root{
  --backdrop:#e6e6e6;
  --paper:#ffffff;
  --bar:#8a8a8a;
  --row-dark:#d9d9d9;
  --row-light:#ececec;
  --ink:#4a4a4a;
  --ink-soft:#8f8f8f;
  --placeholder:#cfcfcf;
  --box:#ffffff;
  --box-line:#7a7a7a;
}
*{box-sizing:border-box;margin:0;padding:0}
html,body{width:1200px;height:801px;overflow:hidden}
body{background:var(--backdrop);font-family:"Open Sans",Arial,sans-serif;color:var(--ink);position:relative}
.page{position:absolute;left:350px;top:25px;width:500px;height:751px;background:var(--paper);padding:14px 20px 0;box-shadow:0 2px 10px rgba(0,0,0,.15)}
.masthead{display:flex;justify-content:space-between;align-items:flex-end;height:62px;margin-bottom:12px}
.brand{display:flex;align-items:center;gap:8px}
.brand-mark{width:34px;height:34px;border-radius:50%;background:var(--ink-soft)}
.brand-name{font-family:"Montserrat",Arial,sans-serif;font-weight:600;font-size:15px;color:var(--ink-soft);line-height:1.15;width:120px}
.date-field{width:182px;height:14px;background:var(--row-light);font-size:8px;padding:1px 6px;margin-bottom:12px}
.section-bar{background:var(--bar);color:#fff;font-weight:700;font-size:8px;text-align:center;height:16px;line-height:16px;border-radius:4px 4px 0 0;text-transform:uppercase}
.section-bar.round{border-radius:8px}
.session-table{display:grid;grid-template-columns:1fr 1fr;gap:0 6px;margin:3px 0 12px}
.session-half{display:grid;grid-template-columns:20px repeat(3,1fr);gap:1px;font-size:7px}
.session-half span{height:13px;line-height:13px;padding-left:4px;background:var(--row-light)}
.session-half .head{background:var(--row-dark);text-align:center;padding:0}
.session-half .blank{background:transparent}
.session-half .num{background:var(--row-dark)}
.session-half .row-b{background:var(--row-dark)}
.severity{background:#f4f4f4;padding:4px 10px 6px;margin-bottom:10px}
.scale-line{position:relative;height:14px;margin:0 20px;border-bottom:1px solid var(--ink-soft)}
.scale-line span{position:absolute;top:0;font-size:7px;transform:translateX(-50%)}
.face-row{display:flex;justify-content:space-between;margin-top:8px}
.face{width:62px;text-align:center;font-size:7px;font-weight:600;color:var(--ink-soft)}
.face-slot{width:26px;height:26px;border-radius:50%;background:var(--placeholder);margin:0 auto 4px}
.regions{display:flex;align-items:flex-start;gap:10px;margin-bottom:12px;padding:0 4px}
.region{width:58px;text-align:center;font-size:6.5px;font-weight:700}
.head-slot{width:46px;height:60px;border-radius:20px 20px 16px 16px;background:var(--placeholder);margin:0 auto 3px}
.mini-scale{display:flex;justify-content:space-between;border-top:1px solid var(--ink);margin-top:3px;padding-top:1px;font-size:4.5px;font-weight:400}
.change-list{margin-left:auto;display:flex;flex-direction:column;gap:3px;font-size:7px}
.change-list .gap{height:4px}
.check{display:inline-block;width:9px;height:9px;border:1px solid var(--box-line);background:var(--box);vertical-align:middle;margin-right:5px}
.grid3{display:grid;grid-template-columns:repeat(3,1fr);gap:1px;margin-top:2px;font-size:7px}
.grid3 div{height:13px;line-height:13px;padding-left:5px;background:var(--row-light)}
.grid3 div.alt{background:var(--row-dark)}
.state-box{display:grid;grid-template-columns:repeat(3,1fr);background:var(--row-light);margin:6px 0 10px;padding:6px 8px;font-size:7px}
.state{display:flex;gap:6px;border-right:1px solid #bbb;padding-left:4px}
.state:last-child{border-right:none}
.state ul{list-style:none;display:flex;flex-direction:column;gap:3px}
.relief{margin-bottom:12px}
.notes-lines{margin-top:4px;display:flex;flex-direction:column;gap:2px}
.notes-lines div{height:12px;background:var(--row-dark)}
.notes-lines div:nth-child(even){background:var(--row-light)}
</style>
</head>
<body>
<main class="page">
  <header class="masthead">
    <div class="brand"><span class="brand-mark"></span><span class="brand-name">The Quillmore Daily Ledger</span></div>
    <div class="date-field">Date</div>
  </header>

  <div class="section-bar">Date</div>
  <div class="session-table">
    <div class="session-half">
      <span class="blank"></span><span class="head">begin</span><span class="head">end</span><span class="head">duration</span>
      <span class="num">1</span><span></span><span></span><span></span>
      <span class="num">2</span><span class="row-b"></span><span class="row-b"></span><span class="row-b"></span>
      <span class="num">3</span><span></span><span></span><span></span>
    </div>
    <div class="session-half">
      <span class="blank"></span><span class="head">begin</span><span class="head">end</span><span class="head">duration</span>
      <span class="num">4</span><span></span><span></span><span></span>
      <span class="num">5</span><span class="row-b"></span><span class="row-b"></span><span class="row-b"></span>
      <span class="num">6</span><span></span><span></span><span></span>
    </div>
  </div>

  <div class="section-bar">Saverity of pain</div>
  <section class="severity">
    <div class="scale-line">
      <span style="left:0%">1</span><span style="left:11.1%">2</span><span style="left:22.2%">3</span><span style="left:33.3%">4</span><span style="left:44.4%">5</span><span style="left:55.5%">6</span><span style="left:66.6%">7</span><span style="left:77.7%">8</span><span style="left:88.8%">9</span><span style="left:100%">10</span>
    </div>
    <div class="face-row">
      <div class="face"><div class="face-slot" role="img" aria-label="Pain scale face: no pain"></div>no pain</div>
      <div class="face"><div class="face-slot" role="img" aria-label="Pain scale face: mild pain"></div>mild pain</div>
      <div class="face"><div class="face-slot" role="img" aria-label="Pain scale face: moderate pain"></div>moderate pain</div>
      <div class="face"><div class="face-slot" role="img" aria-label="Pain scale face: severe pain"></div>severe pain</div>
      <div class="face"><div class="face-slot" role="img" aria-label="Pain scale face: very severe pain"></div>very severe pain</div>
      <div class="face"><div class="face-slot" role="img" aria-label="Pain scale face: worst pain possible"></div>worst pain possble</div>
    </div>
  </section>

  <section class="regions">
    <div class="region"><div class="head-slot" role="img" aria-label="Head diagram highlighting the jaw joint"></div>Joint<div class="mini-scale"><i>1</i><i>2</i><i>3</i><i>4</i><i>5</i><i>6</i><i>7</i><i>8</i><i>9</i><i>10</i></div></div>
    <div class="region"><div class="head-slot" role="img" aria-label="Head diagram highlighting the muscles"></div>Muscles<div class="mini-scale"><i>1</i><i>2</i><i>3</i><i>4</i><i>5</i><i>6</i><i>7</i><i>8</i><i>9</i><i>10</i></div></div>
    <div class="region"><div class="head-slot" role="img" aria-label="Head diagram highlighting the neck"></div>Neck<div class="mini-scale"><i>1</i><i>2</i><i>3</i><i>4</i><i>5</i><i>6</i><i>7</i><i>8</i><i>9</i><i>10</i></div></div>
    <div class="region"><div class="head-slot" role="img" aria-label="Head diagram highlighting forehead tension"></div>Tension<div class="mini-scale"><i>1</i><i>2</i><i>3</i><i>4</i><i>5</i><i>6</i><i>7</i><i>8</i><i>9</i><i>10</i></div></div>
    <div class="region" style="margin-left:14px"><div class="head-slot" role="img" aria-label="Head diagram highlighting the teeth"></div>Teeth<div class="mini-scale"><i>1</i><i>2</i><i>3</i><i>4</i><i>5</i><i>6</i><i>7</i><i>8</i><i>9</i><i>10</i></div></div>
    <div class="change-list">
      <label><span class="check"></span>increased</label>
      <label><span class="check"></span>decreased</label>
      <label><span class="check"></span>no change</label>
      <span class="gap"></span>
      <label><span class="check"></span>increased</label>
      <label><span class="check"></span>decreased</label>
      <label><span class="check"></span>no change</label>
    </div>
  </section>

  <div class="section-bar">Triggers</div>
  <div class="grid3">
    <div class="alt"><span class="check"></span>sleep</div><div class="alt"><span class="check"></span>weather</div><div class="alt"><span class="check"></span>PMS mesntrution</div>
    <div><span class="check"></span>first thing AM</div><div><span class="check"></span>eating</div><div><span class="check"></span>stress at home</div>
    <div class="alt"><span class="check"></span>clanching</div><div class="alt"><span class="check"></span>work</div><div class="alt"><span class="check"></span>stress at work</div>
    <div><span class="check"></span>insomnia</div><div><span class="check"></span>opening wide yamn</div><div><span class="check"></span>other</div>
  </div>
  <div class="state-box">
    <div class="state">My jow was:<ul><li><span class="check"></span>relaxed</li><li><span class="check"></span>clanched</li></ul></div>
    <div class="state">My neck /<br>sholders<br>were:<ul><li><span class="check"></span>relaxed</li><li><span class="check"></span>tense</li></ul></div>
    <div class="state">My breathing<br>was:<ul><li><span class="check"></span>shallow</li><li><span class="check"></span>deep/relaxed</li></ul></div>
  </div>

  <div class="section-bar">Relief measures</div>
  <div class="grid3 relief">
    <div class="alt"><span class="check"></span>deep breathing</div><div class="alt"><span class="check"></span>medication</div><div class="alt"><span class="check"></span>mindful reset</div>
    <div><span class="check"></span>teeth apart/relaxjaw</div><div><span class="check"></span>rest</div><div><span class="check"></span>stabilization exercise</div>
    <div class="alt"><span class="check"></span>self - massage</div><div class="alt"><span class="check"></span>gentle straching</div><div class="alt"><span class="check"></span>other</div>
    <div><span class="check"></span>heat / cold</div><div><span class="check"></span>positive corraction</div><div><span class="check"></span></div>
  </div>

  <div class="section-bar round">Notes and plan to void triggers</div>
  <div class="notes-lines"><div></div><div></div><div></div><div></div><div></div></div>
</main>
</body>
</html>
```